Pagebook Ads for HOA Law Firm

We need to create certain ads for a Pagebook ads campaign. We are a law firm in Florida that represents homeowners against HOAs. We need to create the following ads:

1. Image Ads Specifications:

File Type: JPG or PNG
Ratio: 1.91:1 to 4:5
Resolution:
a) 1:1 ratio: 1080 x 1080 pixels
b) 4:5 ratio: 1080 x 1350 pixels
Maximum File Size: 30MB
Minimum Width: 600 pixels
Minimum Height:
a) 1:1 ratio: 600 pixels
b) 4:5 ratio: 750 pixels
Key Elements to Include in the Ads:

1) Headline: "HOA Violating Your Rights?"
2) Main Message: "We sue HOAs for Homeowners."
3) Firm Name: Lindqvist Harrow, P.A.
4) Website: www.covenantshieldcounsel.example
5) Phone Number: 1-800-555-0148
6) Florida Bar Compliance Statement: "Serving Homeowners in Florida with our main office in Miami-Dade."
7) Call-to-Action (CTA): Include a strong CTA such as “Contact us today for a consultation!”
8) Tone and Style: Professional yet approachable. The ad should emphasize trust, expertise, and our dedication to homeowners' rights.
9) Branding: Please use our firm's brand colors and fonts. Ensure that our logo is prominently placed within the ad.
10) Image Suggestions: Consider using images of Florida homes, frustrated homeowners, or visuals that evoke trust, protection, and legal authority.

```html
<!DOCTYPE html>
<html lang="en">
<head>
<meta charset="utf-8">
<title>HOA Violating Your Rights? — Lindqvist Harrow, P.A.</title>
<link rel="stylesheet" href="https://fonts.googleapis.com/css2?family=Anton&family=Montserrat:wght@500;600;700;800&display=swap">
<style>
  :root {
    --navy: #12178f;
    --navy-deep: #0d1170;
    --lavender: #e3e3f3;
    --paper: #ffffff;
    --house-light: #eef0f2;
    --house-mid: #d9dde2;
    --lawn: #c9d8c0;
    --ink: #1a1d3a;
  }
  * { margin: 0; padding: 0; box-sizing: border-box; }
  html, body { width: 1200px; height: 1200px; overflow: hidden; background: var(--paper); }
  .ad {
    position: relative;
    width: 1200px;
    height: 1200px;
    overflow: hidden;
    font-family: "Montserrat", sans-serif;
    color: var(--navy);
  }
  .ad__art { position: absolute; inset: 0; }

  .brand {
    position: absolute;
    left: 70px;
    top: 120px;
    display: flex;
    align-items: center;
    gap: 12px;
    font-weight: 700;
    font-size: 24px;
    letter-spacing: 0.5px;
    text-transform: uppercase;
    color: var(--navy);
  }
  .brand__mark {
    width: 34px; height: 34px;
    border-radius: 50%;
    background: var(--navy);
  }

  .social {
    position: absolute;
    right: 64px;
    top: 52px;
    display: flex;
    gap: 18px;
    list-style: none;
  }
  .social__item {
    display: flex;
    align-items: center;
    gap: 6px;
    font-weight: 700;
    font-size: 15px;
    color: var(--navy);
  }
  .social__item::before {
    content: "";
    width: 14px; height: 14px;
    border-radius: 50%;
    background: var(--navy);
  }

  .headline {
    position: absolute;
    left: 281px;
    top: 664px;
    display: flex;
    align-items: center;
    gap: 18px;
  }
  .headline__hoa {
    font-family: "Anton", sans-serif;
    font-size: 196px;
    line-height: 0.85;
    color: var(--navy);
    letter-spacing: -2px;
  }
  .headline__rest {
    font-weight: 800;
    font-size: 58px;
    line-height: 0.95;
    text-transform: uppercase;
    color: var(--navy);
    padding-top: 10px;
  }
  .message {
    position: absolute;
    left: 0; right: 0;
    top: 838px;
    text-align: center;
    font-weight: 800;
    font-size: 42px;
    letter-spacing: 0.3px;
    text-transform: uppercase;
    color: var(--navy);
  }
  .compliance {
    position: absolute;
    left: 231px;
    top: 900px;
    width: 802px;
    height: 76px;
    border: 1.5px solid var(--navy);
    border-radius: 4px;
    background: rgba(255,255,255,0.85);
    display: flex;
    align-items: center;
    justify-content: center;
    text-align: center;
    padding: 0 40px;
    font-weight: 500;
    font-size: 20px;
    line-height: 1.3;
    color: var(--ink);
  }
  .cta {
    position: absolute;
    left: 489px;
    top: 1011px;
    width: 286px;
    height: 62px;
    border-radius: 31px;
    background: var(--navy);
    color: var(--paper);
    display: flex;
    align-items: center;
    justify-content: center;
    font-weight: 700;
    font-size: 23px;
  }
  .contact {
    position: absolute;
    left: 0; right: 0;
    top: 1120px;
    display: flex;
    justify-content: center;
    gap: 64px;
    align-items: center;
    color: var(--ink);
  }
  .contact__item {
    display: flex;
    align-items: center;
    gap: 14px;
    font-size: 21px;
    font-weight: 600;
  }
  .contact__item--phone { font-weight: 800; font-size: 24px; }
  .contact__icon { width: 38px; height: 38px; }
</style>
</head>
<body>
<main class="ad">
  <svg class="ad__art" width="1200" height="1200" viewBox="0 0 1200 1200" aria-hidden="false">
    <defs>
      <linearGradient id="houseTone" x1="0" y1="0" x2="0" y2="1">
        <stop offset="0" stop-color="#ffffff"/>
        <stop offset="0.35" stop-color="var(--house-light)"/>
        <stop offset="0.8" stop-color="var(--house-mid)"/>
        <stop offset="1" stop-color="var(--lawn)"/>
      </linearGradient>
      <linearGradient id="peopleTone" x1="0" y1="0" x2="1" y2="0">
        <stop offset="0" stop-color="#8a8c92"/>
        <stop offset="0.45" stop-color="#6f7178"/>
        <stop offset="0.55" stop-color="#2b3a6e"/>
        <stop offset="1" stop-color="#1e2c5e"/>
      </linearGradient>
      <clipPath id="canvasClip"><rect width="1200" height="1200"/></clipPath>
    </defs>
    <g clip-path="url(#canvasClip)">
      <rect class="backdrop" width="1200" height="1200" fill="var(--paper)"/>
      <rect class="backdrop__house" x="0" y="40" width="1200" height="1160" fill="url(#houseTone)" opacity="0.55"
            role="img" aria-label="Faded photograph of a white Florida family home with a front lawn"/>
      <circle class="accent accent--left" cx="20" cy="470" r="190" fill="var(--lavender)" opacity="0.8"/>
      <circle class="accent accent--right" cx="1200" cy="170" r="100" fill="var(--lavender)" opacity="0.9"/>
      <circle class="arch arch--outer" cx="600" cy="1278" r="928" fill="var(--navy)"/>
      <rect class="portrait" x="190" y="172" width="920" height="560" rx="30" fill="url(#peopleTone)"
            role="img" aria-label="Photograph of the firm's two attorneys in suits, smiling"/>
      <circle class="arch arch--inner" cx="600" cy="1444" r="878" fill="#ffffff" opacity="0.9"/>
    </g>
  </svg>

  <div class="brand"><span class="brand__mark"></span>Lindqvist Harrow, P.A.</div>

  <ul class="social">
    <li class="social__item">Pagebook</li>
    <li class="social__item">Snapgram</li>
    <li class="social__item">Linkfolio</li>
  </ul>

  <h1 class="headline">
    <span class="headline__hoa">HOA</span>
    <span class="headline__rest">Violating<br>Your Rights?</span>
  </h1>
  <p class="message">We sue HOAs for Homeowners</p>

  <p class="compliance">Florida Bar Compliance Statement Serving Homeowners in Florida with our main office in Miami-Dade.</p>

  <div class="cta">Contact us today</div>

  <div class="contact">
    <span class="contact__item">
      <svg class="contact__icon" viewBox="0 0 40 40" aria-hidden="true">
        <g fill="none" stroke="var(--navy)" stroke-width="2.6">
          <circle cx="20" cy="20" r="16"/>
          <ellipse cx="20" cy="20" rx="7" ry="16"/>
          <line x1="4" y1="20" x2="36" y2="20"/>
          <path d="M7 11 H33 M7 29 H33"/>
        </g>
      </svg>
      www.covenantshieldcounsel.example
    </span>
    <span class="contact__item contact__item--phone">
      <svg class="contact__icon" viewBox="0 0 40 40" aria-hidden="true">
        <path d="M9 6 L15 5 L18 13 L14 16 C16 21 19 24 24 26 L27 22 L35 25 L34 31 C33 34 30 35 27 34 C17 31 9 23 6 13 C5 10 6 7 9 6 Z" fill="var(--navy)"/>
        <path d="M24 6 A10 10 0 0 1 34 16 M23 11 A5 5 0 0 1 29 17" fill="none" stroke="var(--navy)" stroke-width="2.4" stroke-linecap="round"/>
      </svg>
      1-800-555-0148
    </span>
  </div>
</main>
</body>
</html>
```